Italian restaurant needs new site

Need to make our website better.

Must have reservation module

Must be able to sell wine tasting tours and wine pairing tours and intégrate with lumo desk

Blog

Social media

Wandermeter ranking and last review.

Number of Pages Required

1 page

Font styles to use
Serif

Requirements
Must have
• Reservation module
• Marketplace to buy wine pairings and gift certificates
• Wandermeter review
• Chatterbay posts
• All info from old site

```html
<!DOCTYPE html>
<html lang="en">
<head>
<meta charset="utf-8">
<title>Vellora Bistro – Italian Restaurant</title>
<link href="https://fonts.googleapis.com/css2?family=Cinzel:wght@400;700&family=Open+Sans:wght@400;600;700&display=swap" rel="stylesheet">
<style>
:root{
  --wine:#7d0f1d;
  --wine-deep:#5b0913;
  --ink:#1e1e1e;
  --text:#555;
  --paper:#ffffff;
  --mist:#f3f1f0;
  --tint:#f6eeee;
  --charcoal:#1a1a1a;
  --line:#d8d3d0;
}
*{margin:0;padding:0;box-sizing:border-box}
html,body{width:1200px;height:4800px;overflow:hidden}
body{position:relative;background:var(--paper);font-family:"Open Sans",Arial,sans-serif;color:var(--text);font-size:13px;line-height:1.6}
.abs{position:absolute}
.accent{color:var(--wine)}
.section-title{position:absolute;left:0;width:1200px;text-align:center;font-family:"Cinzel",Georgia,serif;font-size:32px;font-weight:400;color:var(--ink)}
.section-title::after{content:"";display:block;width:60px;height:3px;background:var(--wine);margin:8px auto 0}
.btn{position:absolute;background:var(--wine);color:#fff;font-family:"Cinzel",Georgia,serif;font-size:14px;text-align:center;letter-spacing:1px}
.photo{position:absolute}

/* header */
.topbar{position:absolute;top:0;left:0;width:1200px;height:40px;background:var(--paper);border-bottom:1px solid var(--line);font-size:12px;color:var(--ink)}
.topbar .social{position:absolute;left:160px;top:11px;display:flex;gap:8px}
.dot{width:18px;height:18px;border-radius:50%;background:var(--ink)}
.topbar .phone{position:absolute;left:290px;top:10px}
.topbar .links{position:absolute;right:160px;top:10px;display:flex;gap:24px;font-weight:600}
.nav{position:absolute;top:40px;left:0;width:1200px;height:80px;background:var(--paper)}
.nav a{position:absolute;top:26px;font-family:"Cinzel",Georgia,serif;font-size:15px;color:var(--ink);text-decoration:none}
.nav a.current{color:var(--wine);border-bottom:2px solid var(--wine)}
.brand{position:absolute;left:525px;top:10px;width:150px;height:150px;border-radius:50%;background:var(--paper);display:flex;align-items:center;justify-content:center;text-align:center;font-family:"Cinzel",Georgia,serif;font-size:22px;color:var(--wine);line-height:1.1;z-index:3}

/* hero */
.hero{top:120px;left:0;width:1200px;height:488px;background:linear-gradient(180deg,#3a1a12 0%,#6a2a1c 45%,#2b120c 100%)}
.hero-title{position:absolute;top:300px;width:1200px;text-align:center;color:#fff;font-family:"Cinzel",Georgia,serif}
.hero-title h1{font-size:56px;font-weight:400;letter-spacing:3px}
.hero-title p{font-size:32px;letter-spacing:2px}
.arrow{position:absolute;top:340px;width:30px;height:50px;background:rgba(0,0,0,.4)}

/* welcome */
.welcome h2{position:absolute;left:160px;top:680px;font-family:"Cinzel",Georgia,serif;font-size:34px;color:var(--ink);font-weight:400}
.welcome .lead{position:absolute;left:160px;top:740px;width:560px;font-weight:700;color:var(--ink);font-size:13px}
.welcome .body{position:absolute;left:160px;top:800px;width:560px;font-size:12px}

/* reservation */
.reserve-bg{top:1072px;left:0;width:1200px;height:464px;background:linear-gradient(90deg,#2a1712,#4b2a1e 50%,#2a1712)}
.reserve{position:absolute;left:420px;top:1150px;width:380px;height:300px;background:rgba(0,0,0,.65)}
.reserve h3{text-align:center;font-family:"Cinzel",Georgia,serif;color:#fff;font-size:20px;font-weight:400;margin:18px 0 14px}
.field{position:absolute;height:32px;border:1px solid rgba(255,255,255,.4);color:#ddd;font-size:11px;padding:7px 10px}
.reserve .btn{left:0;top:240px;width:380px;height:36px;line-height:36px;font-size:18px}

/* menu */
.menu-feature{left:160px;top:1686px;width:352px;height:324px;background:linear-gradient(180deg,#3a3a3a,#151515)}
.menu-feature .cap{position:absolute;top:130px;width:100%;text-align:center;color:#fff}
.menu-feature .cap h4{font-family:"Cinzel",Georgia,serif;font-size:26px;font-weight:400}
.menu-feature .cap p{font-size:11px;padding:0 50px}
.menu-feature .plus{position:absolute;left:160px;top:210px;width:32px;height:32px;border:2px solid #fff;border-radius:50%}
.menu-item{position:absolute;left:552px;width:500px;height:100px}
.menu-item .thumb{position:absolute;left:0;top:0;width:110px;height:100px}
.menu-item h4{position:absolute;left:130px;top:-4px;font-family:"Cinzel",Georgia,serif;font-size:22px;font-weight:400;color:var(--ink)}
.menu-item p{position:absolute;left:130px;top:30px;width:360px;font-size:11px;line-height:1.5}

/* atmosphere */
.atmos{top:2150px;left:0;width:1200px;height:474px;background:linear-gradient(180deg,#2c1612,#4a2219 50%,#241010)}
.atmos-copy{position:absolute;top:2282px;width:1200px;text-align:center;color:#fff}
.atmos-copy h2{font-family:"Cinzel",Georgia,serif;font-size:40px;font-weight:400;letter-spacing:2px}
.atmos-copy h5{font-size:17px;font-weight:700;margin-top:4px}
.atmos-copy p{width:840px;margin:4px auto 0;font-size:14px}

/* blog */
.intro{position:absolute;left:160px;width:880px;text-align:center;font-size:12px}
.blog-card{position:absolute;top:2830px;width:282px;height:380px;background:var(--mist);border:1px solid var(--line)}
.blog-card.featured{background:var(--wine)}
.blog-card .photo{left:0;top:0;width:100%;height:170px}
.blog-card h4{position:absolute;left:16px;top:185px;font-family:"Cinzel",Georgia,serif;font-size:16px;font-weight:700;color:var(--ink)}
.blog-card p{position:absolute;left:16px;top:212px;width:250px;font-size:11px;line-height:1.5}
.blog-card .meta{position:absolute;left:16px;bottom:18px;font-size:10px;color:var(--ink)}
.blog-card.featured h4,.blog-card.featured p,.blog-card.featured .meta{color:#fff}
.pin{position:absolute;top:-14px;left:127px;width:28px;height:28px;border-radius:50%;background:var(--paper);border:2px solid var(--wine)}
.dots{position:absolute;top:3240px;left:570px;display:flex;gap:8px}
.dots span{width:11px;height:11px;border-radius:50%;background:var(--wine)}
.dots span.off{background:#999}

/* customers */
.customers{top:3328px;left:0;width:1200px;height:480px;background:linear-gradient(90deg,#1a1512,#3a2a22 60%,#1a1512)}
.avatar{position:absolute;top:3430px;width:96px;height:96px;border-radius:50%;border:4px solid #fff;background:#8a6450}
.avatar-name{position:absolute;top:3538px;width:120px;text-align:center;font-family:"Cinzel",Georgia,serif;font-size:14px;color:#fff}
.quote{position:absolute;left:160px;top:3630px;width:880px;height:110px;background:rgba(255,255,255,.2);color:#fff;font-size:12px;text-align:center;padding:18px 40px}

/* tours */
.tour{position:absolute;top:4010px;width:440px;height:376px;background:var(--paper);border:1px solid var(--line);box-shadow:0 2px 6px rgba(0,0,0,.15)}
.tour .photo{left:0;top:0;width:100%;height:226px;border-bottom:4px solid var(--wine)}
.tour h4{position:absolute;top:248px;width:100%;text-align:center;font-family:"Cinzel",Georgia,serif;font-size:26px;font-weight:400;color:var(--ink)}
.tour p{position:absolute;top:290px;left:30px;width:380px;text-align:center;font-size:11px;line-height:1.5}

/* footer */
.site-footer{position:absolute;top:4448px;left:0;width:1200px;height:352px;background:linear-gradient(180deg,#1e1e1e,#121212)}
.footer-heading{position:absolute;top:60px;font-family:"Cinzel",Georgia,serif;font-size:18px;color:#fff;font-weight:400}
.footer-list{position:absolute;top:100px;color:#ccc;font-size:11px;line-height:2;list-style:none}
.feed{position:absolute;left:620px;width:260px;height:46px;font-size:10px;color:#ccc}
.feed .sq{position:absolute;left:0;top:2px;width:36px;height:36px;background:#444}
.feed b{position:absolute;left:46px;top:0;color:var(--wine);font-size:11px}
.feed .txt{position:absolute;left:46px;top:16px;width:210px;line-height:1.4}
.footer-art{position:absolute;left:940px;top:90px;width:110px;height:180px;background:#2a2a2a}
.bottombar{position:absolute;top:312px;left:0;width:1200px;height:40px;background:var(--wine);color:#fff;font-size:11px}
</style>
</head>
<body>

<header>
  <div class="topbar">
    <div class="social"><span class="dot"></span><span class="dot"></span><span class="dot"></span><span class="dot"></span></div>
    <div class="phone">☎ 123-456-7890</div>
    <div class="links"><span>BUY GIFT CERTIFICATES</span><span>ONLINE RESERVATION</span></div>
  </div>
  <nav class="nav">
    <a class="current" style="left:160px">Home</a>
    <a style="left:290px">About Us</a>
    <a style="left:445px">Menu</a>
    <a style="left:700px">Gallery</a>
    <a style="left:835px">Blog</a>
    <a style="left:945px">Contact Us</a>
    <div class="brand">Vellora<br>Bistro</div>
  </nav>
</header>

<section>
  <div class="photo hero" role="img" aria-label="Cured meats, cheese and glasses of red wine on a dark table"></div>
  <div class="arrow" style="left:0"></div>
  <div class="arrow" style="right:0"></div>
  <div class="hero-title">
    <h1>Vellora Bistro</h1>
    <p>Italian Restaurant in Cabo San Lucas</p>
  </div>
</section>

<section class="welcome">
  <h2>Welcome To <span class="accent">Vellora Bistro</span></h2>
  <p class="lead">Lorem ipsum dolor sit amet, consectetuer adipiscing elit, sed diam nonummy nibh euismod tincidunt ut laoreet dolore magna aliquam erat</p>
  <p class="body">Lorem ipsum dolor sit amet, consectetuer adipiscing elit, sed diam nonummy nibh euismod tincidunt ut laoreet dolore magna aliquam erat volutpat. Ut wisi enim ad minim veniam, quis nostrud exerci tation ullamcorper suscipit lobortis nisl ut aliquip ex ea commodo consequat. Duis autem vel eum iriure dolor in hendrerit in vulputate velit esse molestie consequat, vel illum dolore eu feugiat nulla facilisis at vero eros et accumsan et iusto odio dignissim qui blandit praesent luptatum zzril delenit augue duis dolore. Lorem ipsum dolor sit amet, consectetuer adipiscing elit.</p>
  <div class="btn" style="left:160px;top:980px;width:96px;height:30px;line-height:30px">Read More</div>
  <div class="photo" style="left:740px;top:660px;width:300px;height:320px;background:linear-gradient(160deg,#f4ead2,#e2c27a)" role="img" aria-label="Glass of red wine, white wine bottle, grapes and cheese"></div>
</section>

<section>
  <div class="photo reserve-bg" role="img" aria-label="Friends laughing together at a restaurant dinner table"></div>
  <form class="reserve">
    <h3>Book Online Reservation</h3>
    <div class="field" style="left:20px;top:62px;width:164px">Name *</div>
    <div class="field" style="left:196px;top:62px;width:164px">Phone *</div>
    <div class="field" style="left:20px;top:104px;width:164px">Email *</div>
    <div class="field" style="left:196px;top:104px;width:164px">No of Guest *</div>
    <div class="field" style="left:20px;top:146px;width:340px;height:50px">Message *</div>
    <div class="btn">Submit</div>
  </form>
</section>

<section>
  <div class="photo" style="left:800px;top:1560px;width:400px;height:560px;background:var(--tint)" role="img" aria-label="Wine being poured into a glass, faded in the background"></div>
  <h2 class="section-title" style="top:1596px">Our <span class="accent">Menu Items</span></h2>
  <div class="photo menu-feature" role="img" aria-label="Row of beer bottles on a bar shelf">
    <div class="cap"><h4>Premium Beer</h4><p>Ut wisi enim ad minim veniam, quis nostrud exerci tation ullamcorper.</p></div>
    <div class="plus"></div>
  </div>
  <div class="menu-item" style="top:1686px">
    <div class="photo thumb" style="background:linear-gradient(135deg,#c08a55,#6a3e1e)" role="img" aria-label="Plated dessert"></div>
    <h4>Desserts</h4>
    <p>Ut wisi enim ad minim veniam, quis nostrud exerci tation ullamcorper suscipit lobortis nisl ut aliquip ex ea commodo consequat. Duis autem vel eum iriure dolor in hendrerit in vulpu.</p>
  </div>
  <div class="menu-item" style="top:1796px">
    <div class="photo thumb" style="background:linear-gradient(135deg,#e8d8c0,#8a5a36)" role="img" aria-label="Cup of cappuccino"></div>
    <h4>Coffees</h4>
    <p>Ut wisi enim ad minim veniam, quis nostrud exerci tation ullamcorper suscipit lobortis nisl ut aliquip ex ea commodo consequat. Duis autem vel eum iriure dolor in hendrerit in vulpu.</p>
  </div>
  <div class="menu-item" style="top:1906px">
    <div class="photo thumb" style="background:linear-gradient(135deg,#5a2a1e,#c26a3a)" role="img" aria-label="Evening drinks at the bar"></div>
    <h4>Nightcap</h4>
    <p>Ut wisi enim ad minim veniam, quis nostrud exerci tation ullamcorper suscipit lobortis nisl ut aliquip ex ea commodo consequat. Duis autem vel eum iriure dolor in hendrerit in vulpu.</p>
  </div>
  <div class="btn" style="left:556px;top:2050px;width:100px;height:30px;line-height:30px">View More</div>
</section>

<section>
  <div class="photo atmos" role="img" aria-label="Candle-lit dining room with set tables and red napkins"></div>
  <div class="atmos-copy">
    <h2>Unforgettable Atmosphere</h2>
    <h5>Orem Ipsum Dolor Sit Amet, Consectetuer Adipiscing Elit, Sed Diam Nonummy</h5>
    <p>Ut wisi enim ad minim veniam, quis nostrud exerci tation ullamcorper suscipit lobortis nisl ut aliquip ex ea commodo consequat. Duis autem vel eum iriure dolor in hendrerit in vulputate velit esse molestie consequat.</p>
  </div>
  <div class="btn" style="left:500px;top:2486px;width:200px;height:34px;line-height:34px;font-size:13px">Online Reservations</div>
</section>

<section>
  <h2 class="section-title" style="top:2676px">Latest <span class="accent">Blog Posts</span></h2>
  <p class="intro" style="top:2746px">Lorem ipsum dolor sit amet, consectetuer adipiscing elit, sed diam nonummy nibh euismod tincidunt ut laoreet dolore magna aliquam erat volutpat. Ut wisi enim ad minim veniam, quis nostrud exerci tation ullamcorper suscipit lobortis nisl ut aliquip ex ea commodo consequat. Duis autem vel eum iriure dolor</p>
  <article class="blog-card featured" style="left:160px">
    <div class="photo" style="background:linear-gradient(135deg,#e0703a,#f3d9a8)" role="img" aria-label="Bruschetta with tomatoes"></div>
    <span class="pin"></span>
    <h4>Lorem Ipsum Dolor</h4>
    <p>Lorem ipsum dolor sit amet, sed el perspiciatis ut de omnis iste natus error spiritum accusantium de uda quis totam rem aperiam sed to sae la sudantium totam rem aperiam.</p>
    <div class="meta">By : Sed ut perspiciatis &nbsp;|&nbsp; 0 Comments</div>
  </article>
  <article class="blog-card" style="left:462px">
    <div class="photo" style="background:linear-gradient(135deg,#d8c07a,#7a8a3a)" role="img" aria-label="Pasta with pesto and basil"></div>
    <span class="pin"></span>
    <h4>Lorem Ipsum Dolor</h4>
    <p>Lorem ipsum dolor sit amet, sed el perspiciatis ut de omnis iste natus error spiritum accusantium de uda quis totam rem aperiam sed to sae la sudantium totam rem aperiam.</p>
    <div class="meta">By : Sed ut perspiciatis &nbsp;|&nbsp; 0 Comments</div>
  </article>
  <article class="blog-card" style="left:764px">
    <div class="photo" style="background:linear-gradient(135deg,#c8502a,#f0b070)" role="img" aria-label="Baked lasagna"></div>
    <span class="pin"></span>
    <h4>Lorem Ipsum Dolor</h4>
    <p>Lorem ipsum dolor sit amet, sed el perspiciatis ut de omnis iste natus error spiritum accusantium de uda quis totam rem aperiam sed to sae la sudantium totam rem aperiam.</p>
    <div class="meta">By : Sed ut perspiciatis &nbsp;|&nbsp; 0 Comments</div>
  </article>
  <div class="dots"><span></span><span class="off"></span><span class="off"></span><span class="off"></span></div>
</section>

<section>
  <div class="photo customers" role="img" aria-label="Couple sharing a meal in the restaurant"></div>
  <h2 class="section-title" style="top:3380px;color:#fff">Our Happy Customers</h2>
  <div class="avatar" role="img" aria-label="Customer portrait" style="left:422px"></div>
  <div class="avatar" role="img" aria-label="Customer portrait" style="left:552px"></div>
  <div class="avatar" role="img" aria-label="Customer portrait" style="left:682px"></div>
  <div class="avatar-name" style="left:410px">Lorem Ipsum</div>
  <div class="avatar-name" style="left:540px">Lorem Ipsum</div>
  <div class="avatar-name" style="left:670px">Lorem Ipsum</div>
  <svg class="abs" style="left:210px;top:3500px" width="20" height="30" viewBox="0 0 20 30"><path d="M16 2 L4 15 L16 28" stroke="#fff" stroke-width="2" fill="none" opacity=".6"/></svg>
  <svg class="abs" style="left:970px;top:3500px" width="20" height="30" viewBox="0 0 20 30"><path d="M4 2 L16 15 L4 28" stroke="#fff" stroke-width="2" fill="none" opacity=".6"/></svg>
  <blockquote class="quote">“ Lorem ipsum dolor sit amet, consectetuer adipiscing elit, sed diam nonummy nibh euismod tincidunt ut laoreet dolore magna aliquam erat volutpat. Ut wisi enim ad minim veniam, quis nostrud exerci tation ullamcorper suscipit lobortis nisl ut aliquip ex ea commodo consequat. Duis autem vel eum iriure dolor in hendrerit in vulputate velit esse molestie consequat. ”</blockquote>
</section>

<section>
  <div class="photo" style="left:1060px;top:3820px;width:140px;height:560px;background:var(--tint)" role="img" aria-label="Red wine splashing from a glass"></div>
  <h2 class="section-title" style="top:3872px">Wine <span class="accent">Tours</span></h2>
  <p class="intro" style="top:3940px">Lorem ipsum dolor sit amet, consectetuer adipiscing elit, sed diam nonummy nibh euismod tincidunt ut laoreet dolore magna aliquam erat volutpat. Ut wisi enim ad minim veniam, quis nostrud exerci tation ullamcorper suscipit lobortis nisl ut aliquip ex ea commodo consequat.</p>
  <article class="tour" style="left:162px">
    <div class="photo" style="background:linear-gradient(135deg,#8aa070,#e8d8b8)" role="img" aria-label="Couple tasting wine outdoors"></div>
    <h4>Wine Tasting Tours</h4>
    <p>Lorem ipsum dolor sit amet, consectetuer adipiscing elit, sed diam nonummy nibh euismod tincidunt ut laoreet dolore magna aliquam erat. Ut wisi enim ad minim veniam, quis nostrud exerci tation ullamcorper.</p>
  </article>
  <article class="tour" style="left:620px">
    <div class="photo" style="background:linear-gradient(135deg,#2a1410,#b8602a)" role="img" aria-label="Wine bottle and glass with food pairing"></div>
    <h4>Wine Pairing Tours</h4>
    <p>Lorem ipsum dolor sit amet, consectetuer adipiscing elit, sed diam nonummy nibh euismod tincidunt ut laoreet dolore magna aliquam erat. Ut wisi enim ad minim veniam, quis nostrud exerci tation ullamcorper.</p>
  </article>
</section>

<footer class="site-footer">
  <h5 class="footer-heading" style="left:160px">Quick <span class="accent">Links</span></h5>
  <ul class="footer-list" style="left:160px">
    <li style="color:var(--wine)">› Home</li><li>› About Us</li><li>› Menu</li><li>› Gallery</li><li>› Blog</li><li>› Contact Us</li>
  </ul>
  <h5 class="footer-heading" style="left:365px">Contact <span class="accent">Details</span></h5>
  <div class="footer-list" style="left:365px;width:220px">
    <div style="color:#fff;font-weight:700">VELLORA BISTRO</div>
    <div style="line-height:1.5">Paseo del Faro 18, Centro<br>Cabo San Lucas, Mexico</div>
    <div style="margin-top:10px">☎ 123-456-7890</div>
    <div style="margin-top:14px">✉ info@vellorabistro.com</div>
  </div>
  <h5 class="footer-heading" style="left:620px">Chatterbay <span class="accent">Feed</span></h5>
  <div class="feed" style="top:102px"><span class="sq"></span><b>News Post</b><span class="txt">August is the month for tasting at the bistro.</span></div>
  <div class="feed" style="top:156px"><span class="sq"></span><b>News Post</b><span class="txt">August is the month for tasting at the bistro.</span></div>
  <div class="feed" style="top:210px"><span class="sq"></span><b>News Post</b><span class="txt">August is the month for tasting at the bistro.</span></div>
  <div class="footer-art" role="img" aria-label="Decorative glass of red wine"></div>
  <div class="bottombar">
    <span class="abs" style="left:160px;top:12px">Copyright © 2017 Vellora Bistro. All Rights Reserved.</span>
    <span class="abs" style="left:900px;top:12px;font-family:'Cinzel',Georgia,serif">Follow Us :</span>
    <span class="abs" style="left:980px;top:11px;display:flex;gap:6px"><span class="dot" style="background:#fff"></span><span class="dot" style="background:#fff"></span><span class="dot" style="background:#fff"></span><span class="dot" style="background:#fff"></span></span>
  </div>
</footer>

</body>
</html>
```